Natural Organic soap need packaging design

we need a packaging design for new company based in New Zealand Called 'Bremta Global ltd'.. We manufacture Natural organic soap bars.our main USP is that this soap is made of all natural ingredient and no chemical used and soap is made in New Zealand,so we need a design which look natural,simple,classy and luxury and packaging should reflect that its made in New Zealand.please find attached photos of sample soap.
soap will be in two variant:
1. Pure Manuka Honey soap
2. Goat Milk soap
NOTE: the soap in picture is not actually our soap its just a sample what our soap will look like so please don't make a design with KLOMPP written on it. BREMTA is the soap name.
Target Market(s)
international market. mainly young and kids
Industry/Entity Type
It Company

```html
<!DOCTYPE html>
<html lang="en">
<head>
<meta charset="utf-8">
<title>Bremta Goat Milk Soap Label</title>
<link rel="stylesheet" href="https://fonts.googleapis.com/css2?family=Oswald:wght@400;500;600&family=Open+Sans:wght@400;600&display=swap">
<style>
  :root {
    --ink: #231f20;
    --kraft: #b88f63;
    --paper: #ffffff;
    --rule: #2a2420;
  }
  * { box-sizing: border-box; margin: 0; padding: 0; }
  html, body {
    width: 1200px; height: 1167px; overflow: hidden;
    background: var(--paper);
    font-family: "Open Sans", Arial, sans-serif;
    color: var(--ink);
  }
  .canvas { position: relative; width: 1200px; height: 1167px; }

  /* Flat label */
  .label {
    position: absolute; left: 574px; top: 175px;
    width: 537px; height: 662px;
    background: var(--kraft);
  }
  .label__header {
    position: absolute; left: 0; top: 0; width: 100%; height: 300px;
    background: var(--ink);
    color: var(--paper);
    text-align: center;
  }
  .brand-name {
    font-family: "Oswald", Arial, sans-serif;
    font-weight: 600;
    letter-spacing: 4px;
    line-height: 1;
  }
  .label__header .brand-name { font-size: 88px; margin-top: 88px; }
  .brand-origin {
    font-family: "Open Sans", Arial, sans-serif;
    font-weight: 600;
    letter-spacing: 10px;
    line-height: 1;
  }
  .label__header .brand-origin { font-size: 19px; margin-top: 28px; padding-left: 10px; }

  .info-grid { position: absolute; left: 0; top: 300px; width: 100%; height: 183px; }
  .rule { position: absolute; background: var(--rule); }
  .rule--h { height: 3px; }
  .rule--v { width: 3px; }

  .product-name {
    position: absolute; left: 40px; top: 28px;
    font-family: "Oswald", Arial, sans-serif; font-weight: 500;
    font-size: 32px; letter-spacing: 0.5px;
  }
  .weight {
    position: absolute; left: 40px; top: 119px;
    font-family: "Oswald", Arial, sans-serif; font-weight: 500; font-size: 27px;
  }
  .tagline { position: absolute; left: 124px; top: 121px; font-size: 22px; }
  .product-art {
    position: absolute; left: 326px; top: 14px; width: 190px; height: 150px;
    background: linear-gradient(180deg, #2b2421, #1e1a18);
    border-radius: 6px;
  }

  .usp {
    position: absolute; left: 0; top: 515px; width: 100%;
    text-align: center; font-size: 20px; line-height: 1.35;
  }
  .social { position: absolute; left: 42px; top: 628px; display: flex; gap: 12px; }
  .social__icon { width: 27px; height: 27px; border-radius: 6px; background: var(--ink); }
  .contact {
    position: absolute; right: 40px; top: 626px; text-align: right;
    font-size: 13px; line-height: 1.4;
  }
  .contact__company { font-weight: 600; letter-spacing: 0.5px; }

  /* Standalone logo lockup */
  .lockup {
    position: absolute; left: 806px; top: 952px; width: 300px;
    text-align: center; color: var(--ink);
  }
  .lockup .brand-name { font-size: 64px; }
  .lockup .brand-origin { font-size: 15px; margin-top: 20px; padding-left: 10px; }
</style>
</head>
<body>
<main class="canvas">
  <section class="label" aria-label="Goat milk soap label">
    <header class="label__header">
      <div class="brand-name">BREMTA</div>
      <div class="brand-origin">NEW ZEALAND</div>
    </header>

    <div class="info-grid">
      <span class="rule rule--h" style="left:0;top:0;width:100%"></span>
      <span class="rule rule--h" style="left:0;top:83px;width:304px"></span>
      <span class="rule rule--h" style="left:0;top:180px;width:100%"></span>
      <span class="rule rule--v" style="left:302px;top:0;height:183px"></span>
      <span class="rule rule--v" style="left:104px;top:83px;height:100px"></span>

      <div class="product-name">GOAT MILK SOAP</div>
      <div class="weight">80G</div>
      <div class="tagline">Natural organic</div>
      <div class="product-art" role="img" aria-label="Silhouette illustration of a goat"></div>
    </div>

    <p class="usp">This soap is made of all natural ingredient and<br>no chemical used and soap is made in New</p>

    <div class="social" aria-label="Social media links">
      <span class="social__icon"></span>
      <span class="social__icon"></span>
      <span class="social__icon"></span>
    </div>
    <div class="contact">
      <div>www.bremta.co.nz</div>
      <div class="contact__company">BREMTA GLOBAL LTD</div>
    </div>
  </section>

  <div class="lockup" aria-label="Bremta New Zealand logo">
    <div class="brand-name">BREMTA</div>
    <div class="brand-origin">NEW ZEALAND</div>
  </div>
</main>
</body>
</html>
```